Etiketten-Design für Weinflaschen gesucht
Zielgruppe
Wir sind ein Weingut und suchen für unsere Weinflaschen ein neues Etikettdesign.
Aufgabenstellung
Im Anhang sieht man unsere leeren Weinflaschen mit den neuen Kapseln. Dazu passend suchen wir die Etiketten.
Grundfarbe des Etikettes ist Weiß, Größe ca. 11cm hoch & 9cm breit!
Jede Sorte hat ihrer eigene Farbe - diese ist am Kapsel sichtbar und soll sich auch leicht im Etikett
wieder finden.
Etiketten vom Grunddesign gleich + jedoch nur an STELLEN ANDERS EINGEFÄRBT.
Am Etikett zu finden sollte sein:
- Unser Logo mit Namen (Weingut muss nicht vorhanden sein am Etikett)
- Kirchenlogo
- Sorte von Wein:
(Grüner Veltliner - Grün
Traminer - Blau
Rheinriesling - Orange
Blaufränkisch - Rot
St.Lauerent -Gelb
Zweigelt - Weiß)

```html
<!DOCTYPE html>
<html lang="de">
<head>
<meta charset="utf-8">
<title>Rebenhain – Etikettenserie</title>
<link href="https://fonts.googleapis.com/css2?family=Roboto+Slab:wght@300;400&display=swap" rel="stylesheet">
<style>
  :root {
    --canvas: #ffffff;
    --label: #ffffff;
    --label-edge: #e4e4e4;
    --ink: #2b2b2b;
    --art: #3a3a3a;
    --veltliner: #78b843;
    --traminer: #3c6fbf;
    --riesling: #ec7434;
    --blaufraenkisch: #b81d2a;
    --laurent: #f2c60f;
    --zweigelt: #cfd2d8;
  }
  * { box-sizing: border-box; margin: 0; padding: 0; }
  html, body { width: 1200px; height: 848px; overflow: hidden; background: var(--canvas); }
  .label-row {
    position: absolute; top: 310px; left: 34px;
    display: flex; gap: 20px;
  }
  .label {
    position: relative; width: 172px; height: 228px;
    background: var(--label);
    border: 1px solid var(--label-edge);
    overflow: hidden;
    font-family: "Roboto Slab", Georgia, serif;
    color: var(--ink);
  }
  .brand {
    position: absolute; top: 28px; left: 0; right: 0;
    display: flex; flex-direction: column; align-items: center; gap: 5px;
  }
  .brand-dot { width: 12px; height: 12px; border-radius: 50%; background: var(--accent); }
  .brand-name { font-size: 12px; font-weight: 300; letter-spacing: 0.5px; }
  .variety {
    position: absolute; top: 96px; left: 0; right: 0;
    text-align: center; font-size: 12px; font-weight: 300; letter-spacing: 1.4px;
  }
  .church-art {
    position: absolute; top: 126px; left: 38px; width: 100px; height: 74px;
    background: linear-gradient(180deg, #d9d9d9 0%, #9a9a9a 100%);
    border-radius: 4px 4px 0 0;
  }
  .hill { position: absolute; left: 0; bottom: 0; width: 172px; height: 48px; display: block; }
  .hill path { fill: var(--accent); }
  .veltliner { --accent: var(--veltliner); }
  .traminer { --accent: var(--traminer); }
  .riesling { --accent: var(--riesling); }
  .blaufraenkisch { --accent: var(--blaufraenkisch); }
  .laurent { --accent: var(--laurent); }
  .zweigelt { --accent: var(--zweigelt); }
</style>
</head>
<body>
<main class="label-row">
  <article class="label veltliner">
    <div class="brand"><span class="brand-dot"></span><span class="brand-name">Rebenhain</span></div>
    <p class="variety">Grüner Veltliner</p>
    <div class="church-art" role="img" aria-label="Zeichnung einer Kirche auf einem Hügel mit Bäumen und Vögeln"></div>
    <svg class="hill" viewBox="0 0 172 48" aria-hidden="true"><path d="M0 40 Q80 6 172 10 L172 48 L0 48 Z"/></svg>
  </article>
  <article class="label traminer">
    <div class="brand"><span class="brand-dot"></span><span class="brand-name">Rebenhain</span></div>
    <p class="variety">Traminer</p>
    <div class="church-art" role="img" aria-label="Zeichnung einer Kirche auf einem Hügel mit Bäumen und Vögeln"></div>
    <svg class="hill" viewBox="0 0 172 48" aria-hidden="true"><path d="M0 40 Q80 6 172 10 L172 48 L0 48 Z"/></svg>
  </article>
  <article class="label riesling">
    <div class="brand"><span class="brand-dot"></span><span class="brand-name">Rebenhain</span></div>
    <p class="variety">Rheinriesling</p>
    <div class="church-art" role="img" aria-label="Zeichnung einer Kirche auf einem Hügel mit Bäumen und Vögeln"></div>
    <svg class="hill" viewBox="0 0 172 48" aria-hidden="true"><path d="M0 40 Q80 6 172 10 L172 48 L0 48 Z"/></svg>
  </article>
  <article class="label blaufraenkisch">
    <div class="brand"><span class="brand-dot"></span><span class="brand-name">Rebenhain</span></div>
    <p class="variety">Blaufränkisch</p>
    <div class="church-art" role="img" aria-label="Zeichnung einer Kirche auf einem Hügel mit Bäumen und Vögeln"></div>
    <svg class="hill" viewBox="0 0 172 48" aria-hidden="true"><path d="M0 40 Q80 6 172 10 L172 48 L0 48 Z"/></svg>
  </article>
  <article class="label laurent">
    <div class="brand"><span class="brand-dot"></span><span class="brand-name">Rebenhain</span></div>
    <p class="variety">St.Lauerent</p>
    <div class="church-art" role="img" aria-label="Zeichnung einer Kirche auf einem Hügel mit Bäumen und Vögeln"></div>
    <svg class="hill" viewBox="0 0 172 48" aria-hidden="true"><path d="M0 40 Q80 6 172 10 L172 48 L0 48 Z"/></svg>
  </article>
  <article class="label zweigelt">
    <div class="brand"><span class="brand-dot"></span><span class="brand-name">Rebenhain</span></div>
    <p class="variety">Zweigelt</p>
    <div class="church-art" role="img" aria-label="Zeichnung einer Kirche auf einem Hügel mit Bäumen und Vögeln"></div>
    <svg class="hill" viewBox="0 0 172 48" aria-hidden="true"><path d="M0 40 Q80 6 172 10 L172 48 L0 48 Z"/></svg>
  </article>
</main>
</body>
</html>
```